Korvane Business Cards

We need a business card design. We are a Technology (Audio Visual) design, sales and installation company. Looking for a double sided design, clean

Contact Information for Business Card

Clean, modern look, 2 sided

Font styles to use
Sans Serif

```html
<!DOCTYPE html>
<html lang="en">
<head>
<meta charset="utf-8">
<title>Korvane Business Cards</title>
<link rel="stylesheet" href="https://fonts.googleapis.com/css2?family=Arimo:wght@400;700&display=swap">
<style>
  :root {
    --stage: #2b2b2d;
    --navy: #0b1033;
    --navy-deep: #050922;
    --ink: #1c2f40;
    --orange: #f39a24;
    --paper: #ffffff;
    --text: #1f1f1f;
    --rule: #bdbdbd;
  }
  * { box-sizing: border-box; margin: 0; padding: 0; }
  html, body {
    width: 1200px; height: 900px; overflow: hidden;
    background: var(--stage);
    font-family: "Arimo", Arial, sans-serif;
  }
  .cards {
    width: 1200px; height: 900px;
    display: flex; flex-direction: column;
    align-items: center; justify-content: center; gap: 40px;
  }
  .card {
    width: 588px; height: 336px;
    position: relative; overflow: hidden;
    box-shadow: 0 14px 30px rgba(0,0,0,.45);
  }
  /* Front side */
  .card--front { background: var(--navy-deep); }
  .card__texture {
    position: absolute; inset: 0;
    background:
      radial-gradient(ellipse 70% 55% at 62% 12%, rgba(40,52,110,.55), transparent 70%),
      linear-gradient(170deg, var(--navy) 0%, var(--navy) 45%, var(--navy-deep) 100%);
  }
  .card--front .wordmark {
    position: absolute; left: 0; right: 0; top: 118px;
    text-align: center;
    font-weight: 700; font-size: 86px; letter-spacing: -1px;
    color: var(--paper);
  }
  /* Back side */
  .card--back { background: var(--paper); }
  .card--back .wordmark {
    position: absolute; left: 40px; top: 140px;
    font-weight: 700; font-size: 62px; letter-spacing: -1px;
    color: var(--ink);
  }
  .divider {
    position: absolute; left: 318px; top: 78px;
    width: 1px; height: 180px; background: var(--rule);
  }
  .contact {
    position: absolute; left: 344px; top: 84px;
    color: var(--text);
  }
  .contact__name {
    font-weight: 700; font-size: 19px; color: var(--ink); letter-spacing: .3px;
  }
  .contact__role {
    font-size: 14px; color: var(--orange); margin-top: 2px;
  }
  .contact__list { list-style: none; margin-top: 12px; }
  .contact__item {
    display: flex; align-items: center; gap: 7px;
    font-size: 13.5px; line-height: 20px;
  }
  .contact__item svg { width: 13px; height: 13px; flex: none; }
  .accent { color: var(--orange); }
  .contact__address {
    font-style: normal; font-size: 13.5px; line-height: 19px;
    margin-top: 12px;
  }
</style>
</head>
<body>
<main class="cards">
  <section class="card card--front">
    <div class="card__texture" role="img" aria-label="Dark navy background with a soft flowing abstract wave texture"></div>
    <div class="wordmark">Korvane</div>
  </section>

  <section class="card card--back">
    <div class="wordmark">Korvane</div>
    <div class="divider"></div>
    <div class="contact">
      <div class="contact__name">DANIEL REYES</div>
      <div class="contact__role">Managing Director</div>
      <ul class="contact__list">
        <li class="contact__item">
          <svg viewBox="0 0 24 24" fill="#1c2f40"><path d="M6.6 10.8a15 15 0 0 0 6.6 6.6l2.2-2.2c.3-.3.7-.4 1-.2 1.1.4 2.3.6 3.6.6.6 0 1 .4 1 1V20c0 .6-.4 1-1 1A17 17 0 0 1 3 4c0-.6.4-1 1-1h3.5c.6 0 1 .4 1 1 0 1.3.2 2.5.6 3.6.1.3 0 .7-.2 1z"/></svg>
          (555)214-0398
        </li>
        <li class="contact__item">
          <svg viewBox="0 0 24 24" fill="#1c2f40"><path d="M2 5h20v14H2z"/><path d="M2 5l10 8 10-8" fill="none" stroke="#fff" stroke-width="1.8"/></svg>
          sales@korvane.tech
        </li>
        <li class="contact__item">
          <svg viewBox="0 0 24 24" fill="none" stroke="#1c2f40" stroke-width="2"><circle cx="12" cy="12" r="9.5"/><path d="M2.5 12h19M12 2.5c3 3 3 16 0 19M12 2.5c-3 3-3 16 0 19"/></svg>
          <span>www.<span class="accent">korvane</span>.tech</span>
        </li>
      </ul>
      <address class="contact__address">
        1180 Larkspur Ct. Suite 100<br>
        Alder Falls, Georgia 30999
      </address>
    </div>
  </section>
</main>
</body>
</html>
```